Fenlow Systems

Looking for a web site design to market our services/applications
We write and supply bespoke web applications for the offshore and construction industries
Our initial product is Tiko - rope access equipment management
Our buyers will be Rope Access companies via trade associations such as OLVEN and BLUDE
we have a logo designed see it attached we would like to see crisp professional designs based around these colours and design
we will supply web copy later
looking for home, services, blog, contact us, order and a general template (privacy, site map, T&C) pages
Updates
This payment will be for the homepage only
We can discuss other options (pages) with the successful designer
Regards
Colin
Industry/Entity Type
Construction
Look and feel

```html
<!DOCTYPE html>
<html lang="en">
<head>
<meta charset="utf-8">
<title>Fenlow Systems – Web Applications for Offshore &amp; Construction</title>
<link rel="stylesheet" href="https://fonts.googleapis.com/css2?family=Lato:wght@300;400;700;900&family=Oswald:wght@500;600&family=Signika:wght@600&display=swap">
<style>
:root{
  --purple:#3f1a8c;
  --purple-dark:#2d0f70;
  --blue:#17a0e3;
  --blue-deep:#0f86c9;
  --ink:#222;
  --text:#444;
  --muted:#777;
  --rule:#d8d8d8;
  --grey-band:#e8e8e8;
  --dark:#262626;
  --darker:#191919;
  --white:#fff;
}
*{margin:0;padding:0;box-sizing:border-box}
html,body{width:1200px;height:2219px;overflow:hidden}
body{font-family:"Lato",Arial,sans-serif;color:var(--text);background:var(--white);position:relative}
.abs{position:absolute}
a{color:inherit;text-decoration:none}

/* header */
.topbar{left:0;top:0;width:1200px;height:95px;background:var(--purple)}
.brand{left:132px;top:0;width:296px;height:124px;background:var(--white);border-radius:0 0 8px 8px;box-shadow:0 3px 8px rgba(0,0,0,.3);display:flex;align-items:center;gap:14px;padding-left:34px;z-index:2}
.brand-mark{width:56px;height:56px;background:var(--purple);border-radius:6px}
.brand-name{font-weight:700;font-size:27px;line-height:1.05;color:var(--purple)}
.account{left:872px;top:0;width:196px;height:36px;background:var(--blue);display:flex;align-items:center;justify-content:space-around;color:var(--white);font-size:13px}
.account svg{vertical-align:-2px;margin-right:6px}
.nav{left:520px;top:58px;display:flex;font-size:15px;color:var(--white);letter-spacing:.3px}
.nav a{padding:0 28px;border-left:1px solid rgba(255,255,255,.25);line-height:22px}
.nav a:first-child{border-left:none}

/* hero */
.hero{left:0;top:95px;width:1200px;height:505px;background:linear-gradient(180deg,#1ba6e8,#1596da)}
.hero-scene{left:0;top:0;width:1200px;height:505px;background:linear-gradient(160deg,rgba(255,255,255,.08),rgba(0,40,90,.12))}
.hero-title{left:132px;top:264px;width:420px;font-family:"Oswald",sans-serif;font-weight:600;font-size:31px;line-height:42px;color:var(--ink);letter-spacing:0;white-space:nowrap;z-index:3}
.hero-sub{left:132px;top:326px;width:460px;font-family:"Signika",sans-serif;font-weight:600;font-size:20px;line-height:28px;letter-spacing:2px;color:var(--white);z-index:3}
.btn{display:flex;align-items:center;justify-content:center;background:var(--purple);color:var(--white);font-weight:700}
.hero-btn{left:132px;top:400px;width:145px;height:44px;font-size:17px;border-bottom:3px solid var(--purple-dark)}
.laptop{left:559px;top:195px}
.dots{left:806px;top:542px;display:flex;gap:10px}
.dots i{width:16px;height:16px;border-radius:50%;background:#ddd;border:2px solid #999}
.dots i:first-child{background:#555}

/* section heads */
.sec-title{width:1200px;left:0;text-align:center;font-weight:700;font-size:25px;color:var(--purple)}
.sec-title span{color:var(--blue)}
.sec-rule{left:132px;width:936px;height:1px;background:var(--rule)}

/* welcome */
.welcome-lead{left:132px;top:699px;width:936px;text-align:center;font-weight:700;font-size:13px;color:var(--ink)}
.welcome-body{left:195px;top:728px;width:810px;text-align:center;font-size:13px;line-height:20px}
.welcome-btn{left:545px;top:827px;width:109px;height:31px;font-size:13px}

/* services */
.services{left:0;top:906px;width:1200px;height:310px;background:linear-gradient(180deg,#2b2d33,#3b3833 60%,#4a4030)}
.services .sec-title{top:28px;color:var(--white)}
.services-rule{left:132px;top:72px}
.service{top:114px;width:300px;text-align:center;color:var(--white)}
.service-icon{width:94px;height:84px;margin:0 auto;background:linear-gradient(#fff,#e6e6e6);border-radius:12px;display:flex;align-items:center;justify-content:center}
.service h3{margin-top:24px;font-size:20px;font-weight:700}
.service a{display:block;margin-top:22px;font-size:13px;font-weight:700}

/* product */
.product-shot{left:132px;top:1324px;width:284px;height:205px;border:1px solid #ccc;background:var(--white);padding:10px;box-shadow:0 1px 3px rgba(0,0,0,.1)}
.product-shot div{width:100%;height:100%;background:linear-gradient(135deg,#f4f4f4,#d9d9d9)}
.product-name{left:451px;top:1320px;font-size:22px;font-weight:400;color:#333}
.product-rule{left:451px;top:1354px;width:617px;height:1px;background:#bbb}
.product-lead{left:451px;top:1366px;width:617px;font-weight:700;font-size:13px;color:var(--ink)}
.product-body{left:451px;top:1393px;width:617px;font-size:13px;line-height:20px}
.tag-btn{top:1490px;height:39px;font-size:15px;font-weight:400}

/* blog & news */
.band{left:0;top:1566px;width:1200px;height:318px;background:var(--grey-band)}
.panel-head{top:1595px;height:42px;background:linear-gradient(90deg,#f7f7f7,#efefef)}
.panel-head b{display:inline-flex;align-items:center;height:42px;padding:0 38px 0 14px;background:var(--blue);color:var(--white);font-size:21px;clip-path:polygon(0 0,100% 0,93% 100%,0 100%)}
.arrows{position:absolute;right:4px;top:9px;display:flex}
.arrows i{width:22px;height:24px;border:1px solid #bbb;background:var(--white);display:flex;align-items:center;justify-content:center;font-style:normal;font-size:14px;color:#555}
.post{left:132px;width:460px;height:82px}
.avatar{position:absolute;left:0;top:0;width:84px;height:82px;border:1px solid #ccc;background:var(--white);padding:4px}
.avatar div{width:100%;height:100%;background:linear-gradient(160deg,#8da3b8,#4b5563)}
.post-body{position:absolute;left:99px;top:-4px;width:365px;font-size:13px;line-height:20px}
.post-date{color:var(--muted)}
.post-body b{color:var(--ink)}
.news{left:619px;width:449px}
.news-date{position:absolute;left:0;top:0;width:41px;text-align:center;font-weight:700;font-size:12px;color:var(--white)}
.news-date span{display:block;background:var(--blue);height:20px;line-height:20px}
.news-date strong{display:block;background:var(--purple);height:22px;line-height:22px}
.news-body{position:absolute;left:58px;top:-4px;width:391px;font-size:13px;line-height:21px}
.news-body b{color:var(--ink)}

/* partners */
.partners{left:132px;top:1906px;width:936px;display:flex;justify-content:space-between;align-items:center;font-size:19px;color:#555;font-weight:700}
.partners span{display:flex;align-items:center;gap:6px}
.partners i{width:14px;height:14px;border-radius:50%;background:#888}

/* footer */
.footer{left:0;top:1956px;width:1200px;height:216px;background:var(--dark)}
.foot-brand{left:132px;top:2022px;display:flex;align-items:center;gap:14px}
.foot-brand .mark{width:56px;height:56px;background:#555;border-radius:6px}
.foot-brand .sep{width:1px;height:94px;background:#555}
.foot-brand span{font-weight:700;font-size:27px;line-height:1.05;color:#ddd}
.foot-col{top:1974px;color:#ccc;font-size:13px}
.foot-col h4{font-size:17px;font-weight:400;color:var(--white);padding-bottom:10px;border-bottom:1px solid #444;margin-bottom:12px}
.foot-links li{list-style:none;line-height:26px}
.foot-links li::before{content:"→";margin-right:12px;color:#999}
.msg-text{line-height:19px;margin-bottom:16px}
.msg-input{width:209px;height:30px;background:var(--white);color:#333;padding:7px 8px;font-size:13px}
.msg-btn{margin-top:14px;width:78px;height:26px;background:var(--blue);color:var(--white);font-size:13px;display:flex;align-items:center;justify-content:center}
.social li{list-style:none;display:flex;align-items:center;gap:12px;height:34px}
.social i{width:22px;height:22px;border-radius:50%;background:#666}
.bottombar{left:0;top:2172px;width:1200px;height:47px;background:var(--darker);color:#ddd;font-size:13px}
.bottombar .copy{position:absolute;left:136px;top:15px}
.bottombar .legal{position:absolute;right:132px;top:15px}
.legal a{padding:0 12px;border-left:1px solid #666}
.legal a:first-child{border-left:none}
</style>
</head>
<body>

<header>
  <div class="abs topbar"></div>
  <div class="abs brand"><div class="brand-mark"></div><div class="brand-name">Fenlow<br>Systems</div></div>
  <div class="abs account">
    <a href="#"><svg width="12" height="13" viewBox="0 0 12 13"><rect x="1" y="6" width="10" height="7" fill="#fff"/><path d="M3 6V4a3 3 0 0 1 6 0v2" stroke="#fff" stroke-width="1.6" fill="none"/></svg>Login</a>
    <a href="#"><svg width="14" height="13" viewBox="0 0 14 13"><rect x="1" y="1" width="9" height="11" stroke="#fff" stroke-width="1.4" fill="none"/><path d="M6 8l6-6" stroke="#fff" stroke-width="1.6"/></svg>Register</a>
  </div>
  <nav class="abs nav"><a href="#">HOME</a><a href="#">SERVICES</a><a href="#">BLOG</a><a href="#">CONTACT US</a><a href="#">ORDER</a></nav>
</header>

<section class="abs hero">
  <div class="abs hero-scene" role="img" aria-label="Blue-tinted photo of a construction site with workers"></div>
</section>
<svg class="abs laptop" width="563" height="320" viewBox="0 0 563 320">
  <rect x="53" y="0" width="458" height="303" rx="10" fill="#1c1c1c"/>
  <rect x="66" y="18" width="432" height="270" fill="#3a1f0a" role="img" aria-label="Illustration of a hand holding a phone with connected app icons"/>
  <rect x="66" y="18" width="432" height="270" fill="url(#glow)"/>
  <defs><radialGradient id="glow" cx=".45" cy=".5" r=".6"><stop offset="0" stop-color="#f0a040"/><stop offset="1" stop-color="#1a0d04"/></radialGradient></defs>
  <path d="M0 305h563l-12 12H12z" fill="#d6d6d6"/>
  <rect x="0" y="303" width="563" height="5" fill="#eee"/>
</svg>
<h1 class="abs hero-title">WE PROVIDE WEB APPLICATIONS</h1>
<p class="abs hero-sub">FOR THE OFFSHORE &amp; CONSTRUCTION INDUSTRIES</p>
<a class="abs btn hero-btn" href="#">LEARN MORE</a>
<div class="abs dots"><i></i><i></i><i></i></div>

<section>
  <h2 class="abs sec-title" style="top:633px"><span>WELCOME TO</span> THE CORE GROUP</h2>
  <div class="abs sec-rule" style="top:679px"></div>
  <p class="abs welcome-lead">Lorem ipsum dolor sit amet, consectetur adipisicing elit, sed do eiusmod tem incididunt ut labore et dolore magna aliqua. Ut enim ad minim veniam.</p>
  <p class="abs welcome-body">Duis aute irure dolor in reprehenderitnin voliuptate velit esse cillum dolore eu fugiat nulla pariatur Excepteur sint occaecat cupidatat non proident, sunt in culpa qui officia deserunt mollit anim id est laborum Neque porro quisquam est, qui dolorem ipsum qus consectetur adipisci velit, sed quia non numquam eius modi tempora incidunt ut labore et dol magnam aliquam quaerat voluptatem. Ut enim ad minima veniam, quis nostrum exer ullam corporis suscipit laboriosam nisi ut aliquid ex ea commodi consequatur.</p>
  <a class="abs btn welcome-btn" href="#">LEARN MORE</a>
</section>

<section class="abs services" role="img" aria-label="Dark photo of city skyscrapers">
  <h2 class="abs sec-title">OUR SERVICES</h2>
  <svg class="abs services-rule" width="936" height="10"><path d="M0 0.5H459L468 9L477 0.5H936" stroke="#888" fill="none"/></svg>
  <div class="abs service" style="left:121px">
    <div class="service-icon"><svg width="52" height="40" viewBox="0 0 52 40"><rect x="8" y="2" width="36" height="26" rx="2" stroke="#3f1a8c" stroke-width="3" fill="none"/><path d="M2 32h48l-3 5H5z" fill="#3f1a8c"/><path d="M21 10l-5 5 5 5M31 10l5 5-5 5M28 9l-4 12" stroke="#3f1a8c" stroke-width="2.2" fill="none"/></svg></div>
    <h3>SOFTWARE DEVELOPMENT</h3><a href="#">Read More »</a>
  </div>
  <div class="abs service" style="left:449px">
    <div class="service-icon"><svg width="44" height="46" viewBox="0 0 44 46"><g fill="none" stroke="#3f1a8c" stroke-width="3"><rect x="3" y="3" width="38" height="11"/><rect x="3" y="18" width="38" height="11"/><rect x="3" y="33" width="38" height="11"/></g><g fill="#3f1a8c"><rect x="8" y="7" width="18" height="3"/><rect x="8" y="22" width="18" height="3"/><rect x="8" y="37" width="18" height="3"/></g></svg></div>
    <h3>DATA MANAGEMENT</h3><a href="#">Read More »</a>
  </div>
  <div class="abs service" style="left:776px">
    <div class="service-icon"><svg width="46" height="52" viewBox="0 0 46 52"><g fill="#3f1a8c"><circle cx="23" cy="18" r="12"/><path d="M2 52c0-14 9-20 21-20s21 6 21 20z"/></g><path d="M9 20a14 14 0 0 1 28 0" stroke="#3f1a8c" stroke-width="3" fill="none"/></svg></div>
    <h3>CUSTOMER SUPPORT</h3><a href="#">Read More »</a>
  </div>
</section>

<section>
  <h2 class="abs sec-title" style="top:1252px"><span>OUR</span> PRODUCT</h2>
  <div class="abs sec-rule" style="top:1298px"></div>
  <div class="abs product-shot"><div role="img" aria-label="Software box for Tiko rope access equipment management"></div></div>
  <h3 class="abs product-name">Tiko - Rope Access Equipment Management</h3>
  <div class="abs product-rule"></div>
  <p class="abs product-lead">Sed diam nonummy nibh euismod tincidunt ut laoreet dolore ma aliquam erat volutpatn enim veniam.</p>
  <p class="abs product-body">Lorem ipsum dolor sit amet, consectetur adipiscing elit. Sed blandit mas massa vel mauris sollic dignissim Phasellus ultrice tellus egethop ipsum ornare molestie scelerisque eros.Lorem ipsum dolor si consectetur adipiscing elit. Sed blandit mas massa vel mauris sollicitudin dignissim Duis autem vel eum iriure dolosed di nonmy&nbsp; euismod tincidunt ut laoreet dolore ma aliq volutpat.</p>
  <a class="abs btn tag-btn" href="#" style="left:451px;width:108px">OFFSHORE</a>
  <a class="abs btn tag-btn" href="#" style="left:574px;width:240px">CONSTRUCTION INDUSTRIES</a>
</section>

<section>
  <div class="abs band"></div>
  <div class="abs panel-head" style="left:132px;width:467px"><b>LATEST BLOG</b><div class="arrows"><i>‹</i><i>›</i></div></div>
  <div class="abs panel-head" style="left:619px;width:449px"><b>LATEST NEWS</b><div class="arrows"><i>‹</i><i>›</i></div></div>

  <article class="abs post" style="top:1657px">
    <div class="avatar"><div role="img" aria-label="Author portrait"></div></div>
    <div class="post-body"><div class="post-date">January 1, 2014 - 3:00-4:00pm</div><b>Lorem ipsum dolor sit amet, consectetur adipisicing elit.</b><br>Duis autem vel eum iriurein&nbsp; dolor,sed di nonmy&nbsp; euismod tincidunt ut laoreet dolore ma aliq volutpat.</div>
  </article>
  <article class="abs post" style="top:1773px">
    <div class="avatar"><div role="img" aria-label="Author portrait"></div></div>
    <div class="post-body"><div class="post-date">January 1, 2014 - 3:00-4:00pm</div><b>Lorem ipsum dolor sit amet, consectetur adipisicing elit.</b><br>Duis autem vel eum iriurein&nbsp; dolor,sed di nonmy&nbsp; euismod tincidunt ut laoreet dolore ma aliq volutpat.</div>
  </article>

  <article class="abs news" style="top:1657px">
    <div class="news-date"><span>APR</span><strong>29</strong></div>
    <div class="news-body"><b>lorem ipsum dolor sit amnsectetur</b><br>Lorem ipsum dolor sit amet, consectetur adipiscing elit. Sed blandit mas massa vel mauris sollicitudin dignissim. Phasellus ultrice tellus egethop ipsum ornare molestie scelerisque eros.</div>
  </article>
  <article class="abs news" style="top:1773px">
    <div class="news-date"><span>APR</span><strong>29</strong></div>
    <div class="news-body"><b>lorem ipsum dolor sit amnsectetur</b><br>Lorem ipsum dolor sit amet, consectetur adipiscing elit. Sed blandit mas massa vel mauris sollicitudin dignissim. Phasellus ultrice tellus egethop ipsum ornare molestie scelerisque eros.</div>
  </article>
</section>

<div class="abs partners">
  <span><i></i>VERTEX</span><span>ARCOLINE</span><span>nodal</span><span><i></i>BrightWhite</span><span>Trevik</span><span><i></i>Genova</span><span>Rosmoor</span><span>Greenhollow</span>
</div>

<footer>
  <div class="abs footer"></div>
  <div class="abs foot-brand"><div class="mark"></div><div class="sep"></div><span>Fenlow<br>Systems</span></div>
  <div class="abs foot-col" style="left:429px;width:152px">
    <h4>Site Navigation</h4>
    <ul class="foot-links"><li>Home</li><li>Services</li><li>Blog</li><li>Contact us</li><li>Order</li></ul>
  </div>
  <div class="abs foot-col" style="left:626px;width:209px">
    <h4>Leave us a Message</h4>
    <p class="msg-text">Lorem ipsum dolo consectetuer Ut enim ad minim veniauis.</p>
    <div class="msg-input">Email Address</div>
    <div class="msg-btn">SUBMIT</div>
  </div>
  <div class="abs foot-col" style="left:898px;width:170px">
    <h4>Follow Us</h4>
    <ul class="social"><li><i></i>Friendlane</li><li><i></i>Chirpline</li><li><i></i>Orbitplus</li><li><i></i>Linkfold</li></ul>
  </div>
  <div class="abs bottombar">
    <div class="copy">Copyright © 2014 Fenlow Systems. All Rights Reserved</div>
    <div class="legal"><a href="#">Privacy</a><a href="#">Site Map</a><a href="#">Term &amp; Condition</a></div>
  </div>
</footer>

</body>
</html>
```